Bravik = Difficult

Sto Je Treba Ni Bravik
what must be done, is not difficult...

my mom is Croatian and her name is Marela.

a Croatian expression that I came across 12 years ago is 'what must be done, is not difficult'. yes, it is counter-intuitive. but it helped me to get divorced and then to beat Stage 4 cancer. both seem impossible,

but they they had to be done, so they were not difficult.

so I have started up a new company called:
Bravik Consulting - solving difficult

I'll be working with companies that have a difficult program/project that they haven't launched yet...

I envision possibly a business card that is shaped into a "D" to represent the Croatian word of difficult.

yes, I know this is difficult - welcome to my new world - the difficult challenges are worth solving...

a nod to the red/white design of the Croatian flag would be nice.

```html
<!DOCTYPE html>
<html lang="en">
<head>
<meta charset="utf-8">
<title>Bravik Consulting – Business Card</title>
<link rel="stylesheet" href="https://fonts.googleapis.com/css2?family=Arimo:wght@700&display=swap">
<style>
  :root {
    --flag-red: #ec1c24;
    --flag-white: #ffffff;
    --flag-blue: #213f99;
    --outline-green: #6cbf3f;
    --ink: #111111;
    --page: #ffffff;
  }
  html, body {
    margin: 0;
    padding: 0;
    width: 1200px;
    height: 639px;
    overflow: hidden;
    background: var(--page);
  }
  .card-sheet {
    display: block;
    width: 1200px;
    height: 639px;
  }
  .stripe-red { fill: var(--flag-red); }
  .stripe-white { fill: var(--flag-white); }
  .stripe-blue { fill: var(--flag-blue); }
  .card-outline {
    fill: none;
    stroke: var(--outline-green);
    stroke-width: 2;
  }
  .brand-name,
  .brand-descriptor,
  .holder-name,
  .contact-label {
    font-family: "Arimo", Arial, sans-serif;
    font-weight: 700;
  }
  .brand-name { fill: var(--flag-red); font-size: 62px; }
  .brand-descriptor { fill: var(--flag-red); font-size: 34px; }
  .holder-name { fill: var(--flag-white); font-size: 26px; }
  .contact-label { fill: var(--ink); font-size: 24px; }
</style>
</head>
<body>
<svg class="card-sheet" viewBox="0 0 1200 639" xmlns="http://www.w3.org/2000/svg" aria-label="Bravik Consulting business card, front and back">
  <defs>
    <clipPath id="front-shape">
      <path id="front-path" d="M90,84 H344 A210 210 0 0 1 554 294 V350 A210 210 0 0 1 344 560 H90 Q74 560 74 544 V100 Q74 84 90 84 Z"/>
    </clipPath>
    <clipPath id="back-shape">
      <path id="back-path" d="M850,80 H1094 Q1110 80 1110 96 V540 Q1110 556 1094 556 H850 A210 210 0 0 1 640 346 V290 A210 210 0 0 1 850 80 Z"/>
    </clipPath>
  </defs>

  <!-- Card front -->
  <g class="card-front">
    <g clip-path="url(#front-shape)">
      <rect class="stripe-red" x="70" y="80" width="490" height="156"/>
      <rect class="stripe-white" x="70" y="236" width="490" height="174"/>
      <rect class="stripe-blue" x="70" y="410" width="490" height="154"/>
    </g>
    <use href="#front-path" class="card-outline"/>
    <text class="brand-name" x="180" y="318">BRAVIK</text>
    <text class="brand-descriptor" x="183" y="366">CONSULTING</text>
    <text class="holder-name" x="270" y="452">Your Name Here</text>
  </g>

  <!-- Card back -->
  <g class="card-back">
    <g clip-path="url(#back-shape)">
      <rect class="stripe-red" x="636" y="76" width="480" height="160"/>
      <rect class="stripe-white" x="636" y="236" width="480" height="170"/>
      <rect class="stripe-blue" x="636" y="406" width="480" height="154"/>
    </g>
    <use href="#back-path" class="card-outline"/>
    <text class="contact-label" x="894" y="292" text-anchor="end">Tel:</text>
    <text class="contact-label" x="894" y="324" text-anchor="end">Emai:</text>
    <text class="contact-label" x="894" y="358" text-anchor="end">Web:</text>
  </g>
</svg>
</body>
</html>
```